We need a design for our security installation based business. Our name is K M Security Systems

We need a business card for a security installation based company. We want to look modern and professional. We would like our company logo used and the three main colours to be white, black and orange. We install intruder alarms, cctv and access control. Our preference would be to use the black/orange design on the front and orange/black on the back. Feel free to post variations.

Target Market(s)

Business owners, commercial property and large residential properties

Industry/Entity Type

Business

Contact Information for Business Card

Owen Pelham 07813 592 640

Liam Fenwick 07751 286 419

operations@kmsecuritysystems.co.uk

Intruder Alarms
CCTV
Access Control

Colors
f78f20
000000
ffffff

Requirements
Must have
• Must have the logo on the business card somewhere

```html
<!DOCTYPE html>
<html lang="en">
<head>
<meta charset="utf-8">
<title>K M Security Systems – Business Card</title>
<link rel="stylesheet" href="https://fonts.googleapis.com/css2?family=Exo+2:wght@700&family=Open+Sans:wght@400;600&display=swap">
<style>
  :root {
    --orange: #fb4a05;
    --white: #ffffff;
    --ink: #1a1a1a;
    --backdrop: #2c2e33;
    --card-w: 560px;
    --card-h: 340px;
  }
  * { box-sizing: border-box; margin: 0; padding: 0; }
  html, body {
    width: 1200px; height: 864px; overflow: hidden;
    background: var(--backdrop);
  }
  .canvas {
    width: 1200px; height: 864px;
    display: flex; flex-direction: column; align-items: center; justify-content: center;
    gap: 44px;
  }
  .card {
    position: relative;
    width: var(--card-w); height: var(--card-h);
    overflow: hidden;
  }

  /* Front */
  .card--front { background: var(--orange); }
  .front-name {
    position: absolute; left: 0; right: 0; top: 96px;
    text-align: center;
    font-family: "Exo 2", sans-serif; font-weight: 700;
    font-size: 38px; letter-spacing: 0.5px; line-height: 1.1;
    color: var(--white);
    text-transform: uppercase;
  }
  .services-band {
    position: absolute; left: 0; right: 0; top: 238px; height: 72px;
    background: var(--white);
    display: flex; align-items: center; justify-content: center; gap: 20px;
    font-family: "Open Sans", sans-serif; font-weight: 600;
    font-size: 15px; color: var(--orange);
  }
  .services-band .dot {
    width: 8px; height: 8px; border-radius: 50%; background: var(--orange);
  }

  /* Back */
  .card--back { background: var(--white); }
  .brand {
    position: absolute; left: 0; right: 0; top: 62px;
    display: flex; align-items: center; justify-content: center; gap: 14px;
  }
  .brand-square { width: 26px; height: 26px; background: var(--orange); }
  .brand-name {
    font-family: "Exo 2", sans-serif; font-weight: 700;
    font-size: 32px; line-height: 1.1;
    color: var(--orange); text-transform: uppercase;
    text-align: center;
  }
  .contact {
    position: absolute;
    font-family: "Open Sans", sans-serif;
  }
  .contact-name {
    font-weight: 600; font-size: 19px; color: var(--orange); line-height: 1.3;
  }
  .contact-phone {
    display: flex; align-items: center; gap: 6px;
    font-size: 14px; color: var(--ink);
  }
  .contact--left { left: 40px; top: 168px; }
  .contact--right { right: 40px; top: 236px; text-align: right; }
  .contact--right .contact-phone { justify-content: flex-end; }
  .phone-icon { width: 11px; height: 11px; fill: var(--orange); }
  .rule {
    position: absolute; height: 1px; background: var(--orange);
  }
  .rule--left { left: 40px; width: 320px; top: 226px; }
  .rule--right { right: 40px; width: 290px; top: 296px; }
  .email {
    position: absolute; left: 0; right: 0; top: 262px;
    text-align: center;
    font-family: "Open Sans", sans-serif; font-size: 14px; color: var(--ink);
  }
</style>
</head>
<body>
<main class="canvas">

  <section class="card card--front" aria-label="Business card front">
    <h1 class="front-name">K M Security Systems</h1>
    <div class="services-band">
      <span>Intruder Alarms</span>
      <span class="dot"></span>
      <span>CCTV</span>
      <span class="dot"></span>
      <span>Access Control</span>
    </div>
  </section>

  <section class="card card--back" aria-label="Business card back">
    <div class="brand">
      <span class="brand-square"></span>
      <span class="brand-name">K M Security Systems</span>
    </div>

    <div class="contact contact--left">
      <p class="contact-name">Liam Fenwick</p>
      <p class="contact-phone">
        <svg class="phone-icon" viewBox="0 0 24 24" aria-hidden="true"><path d="M6.6 10.8a15.1 15.1 0 0 0 6.6 6.6l2.2-2.2c.3-.3.7-.4 1-.2 1.1.4 2.3.6 3.6.6.6 0 1 .4 1 1V20c0 .6-.4 1-1 1A17 17 0 0 1 3 4c0-.6.4-1 1-1h3.5c.6 0 1 .4 1 1 0 1.3.2 2.5.6 3.6.1.3 0 .7-.2 1z"/></svg>
        07751 286 419
      </p>
    </div>
    <div class="rule rule--left"></div>

    <p class="email">operations@kmsecuritysystems.co.uk</p>

    <div class="contact contact--right">
      <p class="contact-name">Owen Pelham</p>
      <p class="contact-phone">
        07813 592 640
        <svg class="phone-icon" viewBox="0 0 24 24" aria-hidden="true"><path d="M6.6 10.8a15.1 15.1 0 0 0 6.6 6.6l2.2-2.2c.3-.3.7-.4 1-.2 1.1.4 2.3.6 3.6.6.6 0 1 .4 1 1V20c0 .6-.4 1-1 1A17 17 0 0 1 3 4c0-.6.4-1 1-1h3.5c.6 0 1 .4 1 1 0 1.3.2 2.5.6 3.6.1.3 0 .7-.2 1z"/></svg>
      </p>
    </div>
    <div class="rule rule--right"></div>
  </section>

</main>
</body>
</html>
```